need eczema bath soak label/bag

need you to recreate this please. ai file. recreate this exact image please. ...if you want a big tip, create some different styles.

Colors
0054AA
0677BA
7BADD7
CADEEF
E8F1F8

```html
<!DOCTYPE html>
<html lang="en">
<head>
<meta charset="utf-8">
<title>Eczema Bath Soak – Pouch Label</title>
<link rel="stylesheet" href="https://fonts.googleapis.com/css2?family=Poppins:wght@500;600;700&display=swap">
<style>
  :root {
    --backdrop: #d9d9d9;
    --label-white: #ffffff;
    --ink: #0c2526;
    --sea-mist: #cfece6;
    --sea-aqua: #7fd1c4;
    --sea-teal: #24a99c;
    --sea-deep: #1b8f86;
    --foam: #f4f5f3;
    --foam-blush: #f6e9e3;
    --sand-light: #cdb08b;
    --sand: #bc9d77;
    --sand-dark: #a6875f;
  }
  * { box-sizing: border-box; margin: 0; padding: 0; }
  html, body {
    width: 1200px;
    height: 1200px;
    overflow: hidden;
    background: var(--backdrop);
    font-family: "Poppins", sans-serif;
  }
  .label {
    position: absolute;
    left: 150px;
    top: 50px;
    width: 900px;
    height: 1100px;
    background: var(--label-white);
    overflow: hidden;
  }
  .scene-art {
    position: absolute;
    left: 0;
    top: 150px;
    width: 900px;
    height: 880px;
    background: linear-gradient(
      to bottom,
      rgba(255,255,255,0) 0%,
      var(--sea-mist) 5%,
      var(--sea-aqua) 10%,
      var(--foam) 17%,
      var(--foam-blush) 26%,
      var(--sea-aqua) 31%,
      var(--sea-teal) 36%,
      var(--sea-deep) 40%,
      var(--sea-aqua) 44%,
      var(--foam) 52%,
      var(--foam) 56%,
      var(--sand-light) 62%,
      var(--sand) 80%,
      var(--sand-dark) 100%
    );
  }
  .heading {
    position: absolute;
    top: 78px;
    left: 0;
    width: 100%;
    text-align: center;
    color: var(--ink);
  }
  .heading__kicker {
    display: flex;
    align-items: center;
    justify-content: center;
    gap: 26px;
    font-weight: 600;
    font-size: 44px;
    letter-spacing: 1px;
    line-height: 1;
  }
  .heading__rule {
    width: 160px;
    height: 2px;
    background: var(--ink);
  }
  .heading__title {
    font-weight: 700;
    font-size: 104px;
    letter-spacing: 3px;
    line-height: 1;
    margin-top: 14px;
  }
  .heading__blurb {
    margin: 22px auto 0;
    width: 360px;
    font-weight: 500;
    font-size: 15.5px;
    line-height: 1.45;
  }
  .net-weight {
    position: absolute;
    left: 0;
    width: 100%;
    top: 985px;
    text-align: center;
    font-weight: 600;
    font-size: 21px;
    color: var(--ink);
  }
</style>
</head>
<body>
  <main class="label">
    <div class="scene-art" role="img" aria-label="Photograph of a turquoise ocean wave with white foam washing onto sandy beach"></div>
    <header class="heading">
      <div class="heading__kicker">
        <span class="heading__rule"></span>
        <span>ECZEMA</span>
        <span class="heading__rule"></span>
      </div>
      <h1 class="heading__title">BATH SOAK</h1>
      <p class="heading__blurb">Lorem ipsum dolor sit amet, consectetur adipiscing elit, sed do eiusmod tempor suspendisse ultrices gravida.</p>
    </header>
    <p class="net-weight">Net weight: 500ml</p>
  </main>
</body>
</html>
```